New Townhome community needs for sale sign.

need a 4 foot by 8 foot banner to put on building listing newly constructed townhomes as "coming soon" to market. Construction is scheduled to be completed Dec 2024. Sale of units will begin Spring of 2025.
6 individual townhome units each 2,000 square feet. each unit is 3 bedroom 2.5 bathroom with 2 car garage and each has a rooftop "sky lounge" with amazing views. Gated community. Units available for sale Spring of 2025. Real estate company selling units will be KTL & Associates. Will need KTL & Associates Logo on the banner. Would like to keep with the same blue color scheme as the KTL & Associates logo. phone number on banner to be 480-555-3164. web ktlpartners.example.

```html
<!DOCTYPE html>
<html lang="en">
<head>
<meta charset="utf-8">
<title>Coming Soon – Townhome Banner</title>
<link rel="stylesheet" href="https://fonts.googleapis.com/css2?family=Open+Sans:wght@400;700&family=Roboto+Slab:wght@300;400;800&family=Montserrat:wght@500&display=swap">
<style>
  :root {
    --navy: #0b4463;
    --sky: #2e9fd3;
    --ink: #333333;
    --rule: #444444;
    --paper: #ffffff;
    --backdrop: #c4c4c4;
  }
  * { margin: 0; padding: 0; box-sizing: border-box; }
  html, body {
    width: 1003px; height: 1200px; overflow: hidden;
    background: var(--backdrop);
  }
  .banner {
    position: absolute; left: 51px; top: 375px;
    width: 900px; height: 451px;
    background: var(--paper); overflow: hidden;
  }
  .banner-art { position: absolute; inset: 0; }
  .text { position: absolute; white-space: nowrap; }
  .kicker {
    left: 634px; top: 25px; transform: translateX(-50%);
    font: 500 18px "Montserrat", sans-serif; color: var(--sky); letter-spacing: .3px;
  }
  .headline {
    left: 409px; top: 40px;
    font: 800 61px/1 "Roboto Slab", serif; color: var(--navy);
    text-shadow: 3px 4px 0 var(--sky); letter-spacing: -.5px;
  }
  .feature { font: 400 19px/1.4 "Open Sans", sans-serif; color: var(--ink); }
  .feature b { font-weight: 700; color: var(--sky); }
  .units { left: 407px; top: 123px; }
  .rooms { left: 407px; top: 187px; }
  .lounge { right: 42px; top: 250px; text-align: right; }
  .gated { right: 42px; top: 313px; }
  .rule { position: absolute; height: 1.5px; background: var(--rule); }
  .rule-units { left: 407px; top: 180px; width: 291px; }
  .rule-lounge { left: 567px; top: 310px; width: 291px; }
  .launch {
    left: 607px; top: 350px; transform: translateX(-50%);
    font: 300 17px "Roboto Slab", serif; color: var(--ink);
  }
  .phone {
    left: 600px; top: 385px; transform: translateX(-50%);
    font: 700 22px "Open Sans", sans-serif; color: var(--paper); letter-spacing: 9px;
  }
  .availability {
    left: 600px; top: 413px; transform: translateX(-50%);
    font: 400 24px "Roboto Slab", serif; color: var(--paper);
  }
</style>
</head>
<body>
  <section class="banner">
    <svg class="banner-art" width="900" height="451" viewBox="0 0 900 451">
      <defs>
        <linearGradient id="buildingTones" x1="0" y1="0" x2="0" y2="1">
          <stop offset="0" stop-color="#9fc3e0"/>
          <stop offset=".45" stop-color="#8a8680"/>
          <stop offset=".75" stop-color="#5d6a4a"/>
          <stop offset="1" stop-color="#4b6a2e"/>
        </linearGradient>
      </defs>
      <rect class="contact-band" x="250" y="379" width="650" height="72" fill="var(--navy)"/>
      <path class="photo-frame" d="M0 0 H295 C420 75 430 340 275 451 H0 Z" fill="var(--navy)"/>
      <path class="photo" role="img" aria-label="Photo of modern multi-storey residential buildings with balconies, lawn and walkway under a blue sky"
            d="M0 0 H267 C390 70 400 330 245 451 H0 Z" fill="url(#buildingTones)"/>
    </svg>

    <p class="text kicker">Newly Constructed Townhomes as</p>
    <h1 class="text headline">COMING SOON</h1>

    <p class="text feature units">6 individual townhome units<br><b>each 2,000 square feet.</b></p>
    <div class="rule rule-units"></div>
    <p class="text feature rooms">Each unit is <b>3 bedroom 2.5 bathroom</b><br>with <b>2 car garage.</b></p>
    <p class="text feature lounge">Each has a rooftop <b>"sky lounge"</b><br>with amazing views.</p>
    <div class="rule rule-lounge"></div>
    <p class="text feature gated"><b>Gated community.</b></p>
    <p class="text launch">Sale of units will begin Spring of 2025.</p>

    <p class="text phone">480-555-3164</p>
    <p class="text availability">UNITS AVAILABLE FOR SALE SPRING OF 2025</p>
  </section>
</body>
</html>
```